Cedar Ridge Paving. Chip Seal Done Right

I need my card to have all my basic information on it. Keep it simple. Include web site, phone number and email address. Include phrase Chip Seal Done Right or Cedar Ridge’s Top Paving Company. Keep card simple. Include color and logo. Put all contact info on card. Make card simple and not complicated.
Updates

Here is infuriation yo out in business card

Mark T. Delgado
512.408.7316 cell phone
Markdelgado7@mailbrook.net
www.cedarridgepaving.net

Target Market(s)

Hill Country Texas USA

Industry/Entity Type

Road chip seal

Contact Information for Business Card

We chip seal roads for ranches and property owners

Font styles to use
Serif
Sans Serif
Decorative
Script

Colors
0054AA
0677BA
7BADD7
CADEEF
E8F1F8
EB3D1F
EC4F4E
F09395
F8D3D4
FCEDEE

Requirements
Must have
• Keep it simply
Nice to have
• Logo and all basic info

```html
<!DOCTYPE html>
<html lang="en">
<head>
<meta charset="utf-8">
<title>Cedar Ridge Paving – Business Card</title>
<link href="https://fonts.googleapis.com/css2?family=Montserrat:wght@400;500;600;800;900&display=swap" rel="stylesheet">
<style>
  :root {
    --navy: #141e4e;
    --red: #b01f2e;
    --white: #ffffff;
    --ink-soft: #3a4266;
    --backdrop: #c4c4c4;
  }
  * { box-sizing: border-box; margin: 0; padding: 0; }
  html, body {
    width: 1200px; height: 788px; overflow: hidden;
    background: var(--backdrop);
    font-family: "Montserrat", Arial, sans-serif;
  }
  .sheet {
    width: 1200px; height: 788px;
    display: flex; align-items: center; justify-content: center; gap: 40px;
  }
  .card {
    position: relative;
    width: 540px; height: 309px;
    border-radius: 22px;
    overflow: hidden;
    box-shadow: 0 12px 28px rgba(0,0,0,.25);
  }

  /* Front */
  .card--front { background: var(--white); color: var(--navy); }
  .front__brand {
    position: absolute; left: 34px; top: 34px;
    font-weight: 900; font-size: 26px; line-height: 1.05;
    text-transform: uppercase; letter-spacing: .5px; color: var(--navy);
  }
  .front__accent {
    position: absolute; left: 0; top: 138px;
    width: 14px; height: 44px; background: var(--red);
  }
  .front__person { position: absolute; left: 34px; top: 136px; }
  .person__name {
    font-weight: 800; font-size: 23px; letter-spacing: 1px;
    text-transform: uppercase; color: var(--navy);
  }
  .person__title { font-size: 14px; font-weight: 500; color: var(--ink-soft); margin-top: 2px; }
  .front__contacts {
    position: absolute; left: 34px; top: 206px;
    list-style: none; display: grid; gap: 7px;
  }
  .contact { display: flex; align-items: center; gap: 10px; font-size: 15px; color: var(--navy); }
  .contact__icon { width: 14px; height: 14px; fill: var(--red); flex: none; }

  /* Back */
  .card--back {
    background: var(--navy); color: var(--white);
    display: flex; flex-direction: column; align-items: center; justify-content: center;
  }
  .back__brand {
    font-weight: 900; font-size: 40px; letter-spacing: 1px;
    text-transform: uppercase; color: var(--white); text-align: center;
  }
  .back__rule { width: 300px; height: 2px; background: var(--red); margin: 14px 0 0; }
  .back__tagline {
    position: absolute; bottom: 40px; left: 0; right: 0;
    text-align: center; font-size: 16px; font-weight: 500; letter-spacing: .5px;
  }
</style>
</head>
<body>
<main class="sheet">
  <section class="card card--front" aria-label="Card front">
    <div class="front__brand">Cedar Ridge<br>Paving</div>
    <span class="front__accent"></span>
    <div class="front__person">
      <p class="person__name">Mark T. Delgado</p>
      <p class="person__title">Managing Director</p>
    </div>
    <ul class="front__contacts">
      <li class="contact">
        <svg class="contact__icon" viewBox="0 0 24 24" aria-hidden="true"><path d="M6.6 10.8a15.1 15.1 0 0 0 6.6 6.6l2.2-2.2a1 1 0 0 1 1-.25 11.4 11.4 0 0 0 3.6.57 1 1 0 0 1 1 1V20a1 1 0 0 1-1 1A17 17 0 0 1 3 4a1 1 0 0 1 1-1h3.5a1 1 0 0 1 1 1c0 1.25.2 2.45.57 3.57a1 1 0 0 1-.25 1z"/></svg>
        512.408.7316
      </li>
      <li class="contact">
        <svg class="contact__icon" viewBox="0 0 24 24" aria-hidden="true"><path d="M2 5h20v14H2z M4 7v.5l8 5 8-5V7l-8 5z" fill-rule="evenodd"/></svg>
        Markdelgado7@mailbrook.net
      </li>
      <li class="contact">
        <svg class="contact__icon" viewBox="0 0 24 24" aria-hidden="true"><path d="M12 2a10 10 0 1 0 0 20 10 10 0 0 0 0-20zm6.9 6h-2.9a15.6 15.6 0 0 0-1.4-3.6A8 8 0 0 1 18.9 8zM12 4c.8 1.2 1.5 2.5 1.9 4h-3.8c.4-1.5 1.1-2.8 1.9-4zM4.3 14a8 8 0 0 1 0-4h3.4a16 16 0 0 0 0 4zm.8 2h2.9c.3 1.3.8 2.5 1.4 3.6A8 8 0 0 1 5.1 16zM8 8H5.1a8 8 0 0 1 4.3-3.6C8.8 5.5 8.3 6.7 8 8zm4 12c-.8-1.2-1.5-2.5-1.9-4h3.8c-.4 1.5-1.1 2.8-1.9 4zm2.3-6H9.7a14.6 14.6 0 0 1 0-4h4.6a14.6 14.6 0 0 1 0 4zm.3 5.6c.6-1.1 1.1-2.3 1.4-3.6h2.9a8 8 0 0 1-4.3 3.6zM16.3 14a16 16 0 0 0 0-4h3.4a8 8 0 0 1 0 4z"/></svg>
        www.cedarridgepaving.net
      </li>
    </ul>
  </section>

  <section class="card card--back" aria-label="Card back">
    <h1 class="back__brand">Cedar Ridge Paving</h1>
    <span class="back__rule"></span>
    <p class="back__tagline">Cedar Ridge’s Top Paving Company</p>
  </section>
</main>
</body>
</html>
```